Business card design needed

We require a business card and logo design for our tipper truck business which services the building and agricultural industries, based in Albury-Wodonga, Australia. The business name is 'Bramble Transport' and our business moto is 'if it's tippable, it's doable'.
If a tipper truck is to be included in the logo, the truck must not have a nose ie. the truck must have a flat front.
The moto for the Albury-Wodonga region is 'where the mountains meet the murray' (snowy mountains meet murray river-this may or may not be included in the image design)

Industry/Entity Type

Building

Contact Information for Business Card

BRAMBLE TRANSPORT PTY LTD
Complete Tipper Hire
If it tips, we shift it!
Tom Wexley
0491 570 183
brambletransport@mailnest.com.au
PO Box 819
Kestrelvale NSW 2652
ABN: 27 318 905 442

```html
<!DOCTYPE html>
<html lang="en">
<head>
<meta charset="utf-8">
<title>Bramble Transport Business Cards</title>
<link rel="stylesheet" href="https://fonts.googleapis.com/css2?family=Ubuntu:ital,wght@0,400;0,500;0,700;1,400&display=swap">
<style>
  :root {
    --page-bg: #e4e5e7;
    --card-top: #3a4250;
    --card-bottom: #1f242d;
    --scenery-top: rgba(80, 92, 108, 0);
    --scenery-mid: rgba(80, 92, 108, 0.3);
    --scenery-bottom: rgba(20, 24, 30, 0.25);
    --text-light: #f2f3f5;
    --text-soft: #d6d9de;
    --icon-fill: #e8eaed;
    --icon-ink: #262b34;
    --mark-fill: #c9ccd1;
  }
  * { box-sizing: border-box; margin: 0; padding: 0; }
  html, body { width: 1200px; height: 861px; overflow: hidden; }
  body {
    background: var(--page-bg);
    font-family: "Ubuntu", sans-serif;
    color: var(--text-light);
    position: relative;
  }
  .card {
    position: absolute;
    top: 265px;
    width: 530px;
    height: 330px;
    border-radius: 16px;
    background: linear-gradient(180deg, var(--card-top), var(--card-bottom));
    box-shadow: 0 10px 30px rgba(0, 0, 0, 0.25);
    overflow: hidden;
  }
  .card--front { left: 45px; }
  .card--back { left: 625px; }
  .card__scenery {
    position: absolute;
    left: 0; right: 0; bottom: 0;
    height: 75%;
    background: linear-gradient(180deg, var(--scenery-top), var(--scenery-mid) 40%, var(--scenery-bottom));
  }
  .brand {
    position: absolute;
    display: flex;
    align-items: center;
    gap: 12px;
  }
  .brand__square {
    width: 22px; height: 22px;
    background: var(--mark-fill);
  }
  .brand__name {
    font-weight: 700;
    color: var(--text-light);
    letter-spacing: 0.5px;
    white-space: nowrap;
  }
  .card--front .brand { left: 0; right: 0; top: 120px; justify-content: center; }
  .card--front .brand__name { font-size: 26px; }
  .service {
    position: absolute;
    left: 0; right: 0;
    text-align: center;
    font-weight: 500;
    letter-spacing: 3px;
    color: var(--text-soft);
    white-space: nowrap;
  }
  .card--front .service { top: 196px; font-size: 16px; }
  .tagline {
    position: absolute;
    font-style: italic;
    color: var(--text-soft);
    text-align: center;
  }
  .card--front .tagline { left: 0; right: 0; top: 242px; font-size: 22px; }

  .holder {
    position: absolute;
    left: 32px; top: 62px;
    font-size: 40px;
    font-weight: 700;
    color: var(--text-light);
  }
  .contact {
    position: absolute;
    left: 32px; top: 136px;
    list-style: none;
  }
  .contact__row {
    display: flex;
    align-items: center;
    gap: 14px;
    height: 33px;
    font-size: 16px;
    color: var(--text-soft);
    white-space: nowrap;
  }
  .contact__icon { width: 26px; height: 26px; flex: none; }
  .contact__label { font-weight: 700; font-size: 17px; width: 36px; color: var(--text-light); }
  .card--back .brand { right: 26px; top: 96px; gap: 8px; }
  .card--back .brand__square { width: 14px; height: 14px; }
  .card--back .brand__name { font-size: 15px; }
  .card--back .service { left: auto; right: 26px; width: 170px; top: 132px; font-size: 10px; letter-spacing: 2px; }
  .card--back .tagline { right: 26px; width: 150px; top: 196px; font-size: 15px; line-height: 1.35; }
</style>
</head>
<body>
  <section class="card card--front" aria-label="Business card front">
    <div class="card__scenery" role="img" aria-label="Faint dusk landscape of mountains, trees and river"></div>
    <div class="brand">
      <span class="brand__square"></span>
      <span class="brand__name">BRAMBLE TRANSPORT PTY LTD</span>
    </div>
    <p class="service">Complete Tipper Hire</p>
    <p class="tagline">If it tips, we shift it!</p>
  </section>

  <section class="card card--back" aria-label="Business card back">
    <div class="card__scenery" role="img" aria-label="Faint dusk landscape of river with a rowing boat"></div>
    <h1 class="holder">Tom Wexley</h1>
    <ul class="contact">
      <li class="contact__row">
        <svg class="contact__icon" viewBox="0 0 26 26" aria-hidden="true">
          <circle cx="13" cy="13" r="12" fill="var(--icon-fill)"/>
          <path d="M8 17 L17 8 M8 17 l2 1 M17 8 l1 2" stroke="var(--icon-ink)" stroke-width="2.6" stroke-linecap="round" fill="none"/>
        </svg>
        <span>0491 570 183</span>
      </li>
      <li class="contact__row">
        <svg class="contact__icon" viewBox="0 0 26 26" aria-hidden="true">
          <circle cx="13" cy="13" r="12" fill="var(--icon-fill)"/>
          <rect x="7" y="9" width="12" height="8" fill="var(--icon-ink)"/>
          <path d="M7 9 L13 14 L19 9" stroke="var(--icon-fill)" stroke-width="1.2" fill="none"/>
        </svg>
        <span>brambletransport@mailnest.com.au</span>
      </li>
      <li class="contact__row">
        <svg class="contact__icon" viewBox="0 0 26 26" aria-hidden="true">
          <circle cx="13" cy="13" r="12" fill="var(--icon-fill)"/>
          <rect x="9" y="7" width="8" height="12" fill="var(--icon-ink)"/>
          <rect x="10.5" y="9" width="2" height="2" fill="var(--icon-fill)"/>
          <rect x="13.5" y="9" width="2" height="2" fill="var(--icon-fill)"/>
          <rect x="10.5" y="12.5" width="2" height="2" fill="var(--icon-fill)"/>
          <rect x="13.5" y="12.5" width="2" height="2" fill="var(--icon-fill)"/>
        </svg>
        <span>PO Box 819 Kestrelvale NSW 2652</span>
      </li>
      <li class="contact__row">
        <span class="contact__label">ABN</span>
        <span>27 318 905 442</span>
      </li>
    </ul>
    <div class="brand">
      <span class="brand__square"></span>
      <span class="brand__name">BRAMBLE TRANSPORT</span>
    </div>
    <p class="service">Complete Tipper Hire</p>
    <p class="tagline">If it tips,<br>we shift it!</p>
  </section>
</body>
</html>
```